Venture Capital Investment Firm

We are looking to overhaul our existing website (substantially), with only using the same logos (which we can provide).
We are an investment firm that focuses on making loans to late stage technology companies. Our site should ultimately look like other venture capital firms, and look modern and fresh. We have an existing website www.northvaleloan.com which this will be replacing, although we will be using a lot of the existing written content, and potentially the numbers of pages we will need, we are not wed to anything else. Please feel free to shoot any questions at any time and thank you in advance for your help!
Websites we like as examples:
https://www.tkbrandel.com/
https://www.emberwoodfunds.com/
Target Market(s)
Potential investors who will invest in our firm, as well as potentially companies that are looking to borrow money from us.

```html
<!DOCTYPE html>
<html lang="en">
<head>
<meta charset="utf-8">
<title>Northvale Loan — Investment Partners</title>
<link rel="stylesheet" href="https://fonts.googleapis.com/css2?family=Catamaran:wght@400;500;600&family=Lato:wght@400;700&display=swap">
<style>
:root{
  --navy:#0b0b47;
  --navy-band:#14144c;
  --ink:#1c1c2e;
  --muted:#555;
  --blue:#3b3be8;
  --cta:#3d86f2;
  --card:#efedee;
  --footer:#1b1b1b;
  --map:#8d8d8d;
  --white:#fff;
}
*{margin:0;padding:0;box-sizing:border-box}
html,body{width:1200px;height:4360px;overflow:hidden;background:var(--white)}
body{font-family:"Lato",sans-serif;color:var(--ink);position:relative}
.abs{position:absolute}
h1,h2,h3,h4,.brand,.nav a,.btn{font-family:"Catamaran",sans-serif}
a{color:inherit;text-decoration:none}

/* header */
.site-header{position:absolute;top:0;left:0;width:1200px;height:68px;background:var(--white)}
.brand{position:absolute;display:flex;align-items:center;gap:12px;font-weight:600;color:var(--navy)}
.brand-dot{width:34px;height:34px;border-radius:50%;background:var(--navy)}
.brand-name{font-size:26px;line-height:1;letter-spacing:1px}
.brand-sub{display:block;font-size:9px;letter-spacing:1px;margin-top:3px}
.site-header .brand{left:93px;top:14px}
.nav a{position:absolute;top:24px;font-size:13px;color:#333}
.nav a.active{color:var(--navy);border-bottom:2px solid var(--navy);padding-bottom:2px}
.login{position:absolute;left:963px;top:19px;width:143px;height:30px;background:var(--navy);color:#fff;border-radius:3px;font:600 14px "Catamaran",sans-serif;display:flex;align-items:center;justify-content:center}

/* hero */
.hero{position:absolute;top:68px;left:0;width:1200px;height:532px;background:linear-gradient(90deg,#1b2036 0%,#3d4456 50%,#6c6a68 100%)}
.hero h1{position:absolute;left:93px;top:140px;color:#fff;font-size:48px;font-weight:500;line-height:57px;letter-spacing:1px}
.hero p{position:absolute;left:93px;top:270px;width:600px;color:#fff;font-size:15.5px;line-height:26px}
.btn{display:flex;align-items:center;justify-content:center;font-weight:600;font-size:16px;border-radius:3px}
.hero .btn-primary{position:absolute;left:93px;top:345px;width:120px;height:36px;background:var(--blue);color:#fff}
.hero .btn-outline{position:absolute;left:230px;top:345px;width:120px;height:36px;border:1px solid #fff;color:#fff}
.dots{position:absolute;top:502px;left:571px;display:flex;gap:8px}
.dots span{width:13px;height:13px;border-radius:50%;background:#fff}
.dots span:first-child{background:var(--blue)}

/* section titles */
.sec-title{position:absolute;left:0;width:1200px;text-align:center;font-size:56px;font-weight:500;color:var(--navy);line-height:1}
.sec-sub{position:absolute;left:0;width:1200px;text-align:center}
.rule{position:absolute;left:571px;width:78px;height:4px;background:var(--navy)}

/* about */
.about{position:absolute;top:600px;left:0;width:1200px;height:643px}
.about-photo{position:absolute;left:93px;top:235px;width:478px;height:345px;border-radius:0 22px 0 0;background:linear-gradient(135deg,#eef0f4 0%,#d9dce3 55%,#b9a78a 100%)}
.about-text{position:absolute;left:591px;top:270px;width:510px;font-size:11.5px;line-height:19.5px;color:#444}
.about-text p{margin-bottom:8px}
.about .btn-dark{position:absolute;left:591px;top:499px;width:122px;height:37px;background:var(--navy);color:#fff}

/* strategy */
.strategy{position:absolute;top:1243px;left:0;width:1200px;height:902px;background:var(--navy)}
.strategy .sec-title,.strategy .sec-sub{color:#fff}
.strategy .rule{background:#fff}
.strat-card{position:absolute;top:198px;width:491px}
.strat-img{height:337px;border-radius:0 22px 0 22px}
.strat-card h3{margin-top:12px;font-size:30px;font-weight:500;color:#fff}
.strat-card p{margin-top:6px;font-size:12px;line-height:19.5px;color:#e8e8f2}
.more{display:inline-block;margin-top:10px;font-size:12.5px;font-weight:700;color:#fff}
.view-all{position:absolute;left:506px;top:780px;width:188px;height:49px;border:1.5px solid #fff;color:#fff;border-radius:3px;font-weight:500}

/* team */
.team{position:absolute;top:2145px;left:0;width:1200px;height:627px}
.member{position:absolute;top:132px;width:320px;text-align:center}
.member-photo{height:352px;border-radius:22px 22px 0 0;background:linear-gradient(180deg,#2b2b2b 0%,#6f6f6f 60%,#3a3a3a 100%)}
.member h3{margin-top:8px;font-size:26px;font-weight:400;color:#222;line-height:1.1}
.member .role{font-size:12px;color:var(--navy)}
.social{display:flex;justify-content:center;gap:7px;margin-top:7px}
.social span{width:18px;height:18px;border-radius:50%;background:var(--navy)}

/* cta */
.cta{position:absolute;top:2772px;left:0;width:1200px;height:256px;background:var(--navy-band)}
.cta h2{position:absolute;top:50px;left:0;width:1200px;text-align:center;color:#fff;font-size:31px;font-weight:400;line-height:41px}
.cta .btn{position:absolute;left:525px;top:159px;width:151px;height:47px;background:var(--cta);color:#fff;font-weight:400;font-size:17px}

/* news */
.news{position:absolute;top:3028px;left:0;width:1200px;height:597px}
.news-card{position:absolute;top:143px;width:324px;height:393px;background:var(--card);padding:20px 17px}
.news-img{height:242px;border-radius:0 18px 0 0}
.news-card time{display:block;margin-top:24px;font-size:12px;color:#333;letter-spacing:.3px}
.news-card h4{margin-top:6px;font-size:16px;font-weight:500;line-height:22px;color:#222}
.news-card .more{margin-top:4px;font-size:11.5px;color:#333}

/* footer */
.site-footer{position:absolute;top:3625px;left:0;width:1200px;height:267px;background:var(--footer);color:#ddd}
.site-footer .brand{left:445px;top:68px;color:#fff}
.site-footer .brand-dot{background:#fff;width:44px;height:44px}
.site-footer .brand-name{font-size:36px}
.site-footer .brand-sub{font-size:11px}
.foot-nav{position:absolute;top:158px;left:0;width:1200px;text-align:center;font-size:13px}
.foot-nav span{margin:0 14px;color:#aaa}
.copy{position:absolute;top:196px;left:0;width:1200px;text-align:center;font-size:13px}

.map{position:absolute;top:3892px;left:0;width:1200px;height:468px;background:linear-gradient(160deg,#a8a8a8 0%,#8a8a8a 50%,#6f6f6f 100%)}
.pin{position:absolute;left:549px;top:208px}
</style>
</head>
<body>

<header class="site-header">
  <a class="brand" href="#"><span class="brand-dot"></span><span><span class="brand-name">NORTHVALE LOAN</span><span class="brand-sub">INVESTMENT PARTNERS, LLC</span></span></a>
  <nav class="nav">
    <a class="active" href="#" style="left:464px">Home</a>
    <a href="#" style="left:543px">Strategy</a>
    <a href="#" style="left:637px">About Us</a>
    <a href="#" style="left:735px">Team</a>
    <a href="#" style="left:812px">News</a>
    <a href="#" style="left:889px">Contact</a>
  </nav>
  <a class="login" href="#">Investors Login</a>
</header>

<section class="hero" role="img" aria-label="Business team meeting in a modern office">
  <h1>WE ARE SMART<br>INVESTMENT COMPANI</h1>
  <p>Northvale Loan is a private investment firm unique in its dual focus on life science and technology credit opportunities.</p>
  <a class="btn btn-primary" href="#">Read More</a>
  <a class="btn btn-outline" href="#">Contact Us</a>
  <div class="dots"><span></span><span></span><span></span></div>
</section>

<section class="about">
  <h2 class="sec-title" style="top:58px">About Us</h2>
  <p class="sec-sub" style="top:115px;font:400 30px 'Catamaran',sans-serif;color:var(--navy)">Northvale Loan Started With A Big Idea:</p>
  <p class="sec-sub" style="top:157px;font-size:16px;color:#555">Finance Proven Innovation With A Different Approach</p>
  <div class="rule" style="top:194px"></div>
  <div class="about-photo" role="img" aria-label="Stack of coins on a financial chart"></div>
  <div class="about-text">
    <p>Northvale Loan is a private investment firm unique in its dual focus on life science and technology credit opportunities. Our ambidextrous approach to investing reflects a broad recognition and appreciation for the critical role intellectual property plays in the successful commercialization of products. We apply our extensive industry expertise to assess the revenue visibility created by these assets and offer a range of creative financing solutions.</p>
    <p>A pioneer in providing life science structured credit beginning in 2004, the Northvale team was the first to introduce flexible structured credit to the technology sector in 2014. Our team was also early to recognize the potential of "non-core" assets beyond drug royalties, acquiring over $300M of branded generics offering predictable cash flows from large pharmaceutical firms and partnering with entrepreneurial teams to successfully manage these brands.</p>
  </div>
  <a class="btn btn-dark" href="#">Read More</a>
</section>

<section class="strategy">
  <h2 class="sec-title" style="top:60px">Strategy</h2>
  <p class="sec-sub" style="top:127px;font-size:16px">We Provide Flexible Capital To Innovative Companies And Their Investors</p>
  <div class="rule" style="top:158px"></div>
  <article class="strat-card" style="left:93px">
    <div class="strat-img" role="img" aria-label="Hands pointing at charts on a whiteboard" style="background:linear-gradient(135deg,#dfe6f2 0%,#9fb3d6 60%,#3e5fa8 100%)"></div>
    <h3>Industry Focus</h3>
    <p>Our focus spans the life science and technology industries, two sectors where intellectual property (IP) is an integral driver of asset and enterprise value.</p>
    <p>Our broad experience in investing, technology evaluation, and product forecasting affords us a unique understanding of the value of assets in these dynamic sectors, allowing us to see value where others cannot.</p>
    <a class="more" href="#">Read More &rarr;</a>
  </article>
  <article class="strat-card" style="left:615px">
    <div class="strat-img" role="img" aria-label="Hand using a calculator over financial papers" style="background:linear-gradient(135deg,#f1efea 0%,#c9c6c0 55%,#6f7f95 100%)"></div>
    <h3>Transaction Types</h3>
    <p>Northvale's proven strategy focuses on identifying opportunities where demonstrated commercial success has established underlying asset or enterprise value prior to our investment. We tailor our financing solutions to each situation with the goal of preserving our partners' ownership interests, aligning incentives, and providing operating flexibility to build businesses of value.</p>
    <a class="more" href="#">Read More &rarr;</a>
  </article>
  <a class="btn view-all" href="#">View All Strategy</a>
</section>

<section class="team">
  <h2 class="sec-title" style="top:56px">Our Team</h2>
  <article class="member" style="left:93px">
    <div class="member-photo" role="img" aria-label="Portrait of Miles Harrow"></div>
    <h3>Miles Harrow</h3><p class="role">Life Sciences, Technology</p>
    <div class="social"><span></span><span></span><span></span></div>
  </article>
  <article class="member" style="left:438px">
    <div class="member-photo" role="img" aria-label="Portrait of Devan Okafor"></div>
    <h3>Devan Okafor</h3><p class="role">Technology</p>
    <div class="social"><span></span><span></span><span></span></div>
  </article>
  <article class="member" style="left:786px">
    <div class="member-photo" role="img" aria-label="Portrait of Tobias Lind"></div>
    <h3>Tobias Lind</h3><p class="role">Chief Operating Officer</p>
    <div class="social"><span></span><span></span><span></span></div>
  </article>
</section>

<section class="cta">
  <h2>We Are A Global Structured Credit Investment Firm Focused On The<br>Healthcare And Technology Industries</h2>
  <a class="btn" href="#">Contact Us</a>
</section>

<section class="news">
  <h2 class="sec-title" style="top:56px">Recent News</h2>
  <article class="news-card" style="left:93px">
    <div class="news-img" role="img" aria-label="Hands reviewing charts on a clipboard" style="background:linear-gradient(135deg,#cfd6e2 0%,#8e9bb3 60%,#3c4252 100%)"></div>
    <time>APRIL 30, 2018</time>
    <h4>Northvale completes structured debt investment in Brightloop</h4>
    <a class="more" href="#">Read More &rarr;</a>
  </article>
  <article class="news-card" style="left:438px">
    <div class="news-img" role="img" aria-label="Glasses, calculator and coins on a desk" style="background:linear-gradient(135deg,#ececec 0%,#c8c8c8 55%,#a58f62 100%)"></div>
    <time>APRIL 4, 2016</time>
    <h4>Corvane Semiconductor acquired by Tallwave for $55,000,000</h4>
    <a class="more" href="#">Read More &rarr;</a>
  </article>
  <article class="news-card" style="left:782px">
    <div class="news-img" role="img" aria-label="Team working over charts on a wooden table" style="background:linear-gradient(135deg,#b9925f 0%,#d8d2c8 50%,#5b6f99 100%)"></div>
    <time>JULY 25, 2015</time>
    <h4>Northvale closes inaugural $100,000,000 investment vehicle</h4>
    <a class="more" href="#">Read More &rarr;</a>
  </article>
</section>

<footer class="site-footer">
  <a class="brand" href="#"><span class="brand-dot"></span><span><span class="brand-name">NORTHVALE LOAN</span><span class="brand-sub">INVESTMENT PARTNERS, LLC</span></span></a>
  <nav class="foot-nav">Home<span>|</span>Strategy<span>|</span>About Us<span>|</span>Team<span>|</span>News<span>|</span>Contact</nav>
  <p class="copy">&copy; 2019 Northvale Investment Partners LLC.&nbsp; All Rights Reserved</p>
</footer>

<div class="map" role="img" aria-label="Map of the bay area showing the office location">
  <svg class="pin" width="24" height="34" viewBox="0 0 24 34"><path d="M12 0C5.4 0 0 5.3 0 11.9 0 20.8 12 34 12 34s12-13.2 12-22.1C24 5.3 18.6 0 12 0z" fill="#1b1b1b"/><circle cx="12" cy="12" r="4.5" fill="#8d8d8d"/></svg>
</div>

</body>
</html>
```